Business Card Design for Law firm - already have logo

Now that we have a logo, we need a business card design - our logo is attached -it is salaryman font if that helps - we would like a file that can be uploaded to cardquill (www.cardquill-example.com) using the logo and with the following information on it:
Quenby Law Firm, P.C.
Delwyn Quenby, Esq.
5817 SW 19th Ave.
Millbrook, OR 97418
971.555.0142 phone
971.555.0187 fax
del@quenby-example.net
Voxlink: delquenby
Talkwave: delwyn.quenby@mailbox-example.com
Target Market(s)
our business cards are distributed to corporate executives, technology professionals and healthcare providers
Industry/Entity Type
Business
Look and feel

```html
<!DOCTYPE html>
<html lang="en">
<head>
<meta charset="utf-8">
<title>Quenby Law Firm – Business Card</title>
<link rel="stylesheet" href="https://fonts.googleapis.com/css2?family=Arimo:wght@400&display=swap">
<style>
  :root {
    --page: #ffffff;
    --card-dark: #2f2f2f;
    --card-light: #8a8a8a;
    --ink: #111111;
    --ink-soft: #161616;
    --emblem: rgba(255, 255, 255, 0.05);
    --divider: #1a1a1a;
  }
  * { margin: 0; padding: 0; box-sizing: border-box; }
  html, body {
    width: 1200px;
    height: 900px;
    overflow: hidden;
    background: var(--page);
    font-family: "Arimo", Arial, sans-serif;
  }
  .canvas { position: relative; width: 1200px; height: 900px; }
  .card {
    position: absolute;
    left: 0;
    top: 65px;
    width: 1200px;
    height: 763px;
    background: linear-gradient(90deg, var(--card-dark) 0%, #5a5a5a 45%, var(--card-light) 100%);
    border-radius: 0 145px 0 145px;
    overflow: hidden;
  }
  .emblem {
    position: absolute;
    left: 280px;
    top: 290px;
    width: 625px;
    height: 460px;
  }
  .holder-name {
    position: absolute;
    left: 35px;
    top: 30px;
    font-size: 22px;
    color: #ffffff;
  }
  .firm-mark {
    position: absolute;
    left: 178px;
    top: 80px;
    width: 810px;
    height: 195px;
    display: flex;
    align-items: center;
    justify-content: center;
    font-size: 150px;
    letter-spacing: 28px;
    color: var(--ink);
    line-height: 1;
  }
  .firm-type {
    position: absolute;
    left: 830px;
    top: 297px;
    font-size: 27px;
    color: var(--ink);
    letter-spacing: 0.5px;
  }
  .address {
    position: absolute;
    left: 0;
    width: 1200px;
    top: 405px;
    text-align: center;
    font-size: 24px;
    line-height: 28px;
    color: var(--ink-soft);
    padding-left: 10px;
  }
  .contact-row {
    position: absolute;
    left: 0;
    width: 1200px;
    display: flex;
    align-items: center;
    font-size: 24px;
    color: var(--ink-soft);
  }
  .contact-row .left { width: 572px; text-align: right; }
  .contact-row .divider {
    width: 1px;
    height: 32px;
    margin: 0 42px;
    border-left: 2px dotted var(--divider);
  }
  .contact-row.phones { top: 517px; }
  .contact-row.online { top: 585px; }
  .contact-row.online .divider { height: 40px; }
  .chat {
    position: absolute;
    left: 0;
    width: 1200px;
    top: 660px;
    text-align: center;
    font-size: 24px;
    color: var(--ink-soft);
    padding-left: 50px;
  }
</style>
</head>
<body>
<div class="canvas">
  <div class="card">
    <svg class="emblem" role="img" aria-label="Faint scales of justice emblem" viewBox="0 0 625 460">
      <rect x="0" y="0" width="625" height="460" rx="40" fill="var(--emblem)"/>
    </svg>

    <p class="holder-name">PC Delwyn Quenby,</p>

    <div class="firm-mark">QUENBY</div>
    <p class="firm-type">LAW FIRM</p>

    <p class="address">Esq. 5817 SW 19th Ave.<br>Millbrook, OR 97,418th</p>

    <div class="contact-row phones">
      <span class="left">Phone :- 971l555l0142</span>
      <span class="divider"></span>
      <span class="right">Fax :- 971.555.0187</span>
    </div>

    <div class="contact-row online">
      <span class="left">Del@quenby-example.net</span>
      <span class="divider"></span>
      <span class="right">Voxlink: Delquenby</span>
    </div>

    <p class="chat">Talkwave: delwyn.quenby @ mailbox-example. com</p>
  </div>
</div>
</body>
</html>
```